Website on Hubspot CMS -Boutique consulting firm focused on the events and event tech industries

Design website for our business using Hubspot CMS. Some pages already done. We would like those tweaked to match your recommended design. We also would like landing pages created for four business services offerings. We have a color palette and logo.

Our current website can be found here: www.qlvadvisors.co

QLV Advisors has four service lines:
1. Outsourced Sales
2. Harbor Ledger Strategic Consulting
3. Gridweave Strategic Consulting
4. QLV VIP

Target Market(s)

event organizers, media companies, corporate event marketers, event tech organizations

Industry/Entity Type

Consulting

Coding

Coded - Design and coding required

Number of Pages Required

5+ page

Font styles to use
Sans Serif

Requirements
Must have
• This will be a website built using Hubspot CMS. If you are not familiar with this, please do not participate as we will not be able to use your designs.
SEO optimized
Landing pages with lead capture leading to content downloads
Each service line needs its own page/s with cta's
Highly visual, modern, bold
Navigational areas: Home, Services, Resources, Events, Blog, About Us
Content formats: video, podcasts, content downloads
Will need at least 4 landing pages in addition to the website for each service line plus templates in case we need to update with new copy
We have or own color palette and logo as well as logos for Harbor Ledger and Gridweave. Those colors must be used.
Font can be modified
We need to have a conversation with the designer that is chosen to go over each service line and also understand what kind of images we should be uploading.
Nice to have
• We would really like the site to reflect the following words:
Bold
Future focused
Results oriented
Hyper focused on the events and event technology sectors (sub sectors: corporate event marketers and B2B media companies).
Should not have
• Flat one page design

```html
<!DOCTYPE html>
<html lang="en">
<head>
<meta charset="utf-8">
<title>QLV Advisors – Home</title>
<link href="https://fonts.googleapis.com/css2?family=Roboto:wght@300;400;500&family=Arimo:wght@400&display=swap" rel="stylesheet">
<style>
:root{
  --red:#e52a12;
  --dark:#1b1b1b;
  --ink:#333333;
  --muted:#555555;
  --soft:#f3f3f3;
  --white:#ffffff;
  --button:#333333;
}
*{box-sizing:border-box;margin:0;padding:0}
html,body{width:724px;height:1200px;overflow:hidden}
body{position:relative;background:var(--white);font-family:'Roboto',sans-serif;color:var(--ink)}
.site-header{position:absolute;top:0;left:0;width:724px;height:74px;background:rgba(20,20,20,.85);z-index:2}
.brand{position:absolute;left:67px;top:24px;font-family:'Roboto',sans-serif;font-weight:500;font-size:19px;color:var(--red)}
.main-nav{position:absolute;top:32px;left:0;width:724px}
.main-nav a{position:absolute;font-size:8.4px;font-weight:500;color:var(--white);text-decoration:none;letter-spacing:.1px;white-space:nowrap}
.main-nav a.active{color:var(--red)}
.hero{position:absolute;top:0;left:0;width:724px;height:475px}
.hero-photo{position:absolute;inset:0;background:linear-gradient(120deg,#3a3128 0%,#2a2624 35%,#4a3a2c 60%,#222 100%)}
.hero-title{position:absolute;left:66px;top:215px;font-size:33px;font-weight:500;color:var(--white)}
.hero-sub{position:absolute;left:66px;top:262px;font-size:16.5px;font-weight:400;color:var(--white);line-height:27px}
.hero-sub sup{font-size:8px;vertical-align:top;position:relative;top:2px}
.contact-card{position:absolute;left:423px;top:126px;width:233px;height:309px;background:var(--red);box-shadow:0 0 0 3px rgba(80,80,80,.4)}
.contact-card h2{text-align:center;font-size:15.5px;font-weight:500;color:var(--white);margin-top:18px;height:23px}
.contact-card .rule{height:1px;background:rgba(255,255,255,.2);margin-top:0}
.field{position:absolute;left:12px;width:209px;height:30.5px;background:var(--white);font-size:8.4px;color:var(--ink);padding:10px 10px}
.field.message{height:73px}
.submit{position:absolute;left:12px;top:252px;width:209px;height:30.5px;background:var(--button);color:var(--white);font-size:9.5px;font-weight:500;text-align:center;line-height:30.5px}
.section-title{font-size:23px;font-weight:300;color:var(--ink);white-space:nowrap}
.section-title em{font-style:normal;color:var(--red)}
.services .section-title{position:absolute;top:508px;left:0;width:724px;text-align:center}
.services .underline{position:absolute;top:543px;left:346px;width:31px;height:1px;background:var(--red)}
.service-card{position:absolute;top:607px;width:141px;height:186px;background:var(--white);border:1px solid #eee;box-shadow:0 1px 3px rgba(0,0,0,.08);text-align:center}
.service-icon{position:absolute;left:29px;top:-35px;width:82px;height:82px;border-radius:50%;background:var(--red)}
.service-card h3{position:absolute;top:62px;left:4px;right:4px;font-size:9.3px;font-weight:500;line-height:15.5px;color:var(--ink)}
.service-card p{position:absolute;left:6px;right:6px;font-family:'Arimo',sans-serif;font-size:8.2px;line-height:15.5px;color:var(--muted)}
.welcome{position:absolute;top:841px;left:0;width:724px;height:306px;background:var(--soft)}
.welcome .section-title{position:absolute;left:67px;top:32px}
.welcome .underline{position:absolute;left:67px;top:67px;width:31px;height:1px;background:var(--red)}
.welcome p{position:absolute;font-family:'Arimo',sans-serif;font-size:8.2px;line-height:16px;color:var(--muted)}
.welcome .lead{left:67px;top:90px;width:590px}
.welcome .detail{left:67px;top:163px;width:347px;text-align:justify}
.welcome-brand{position:absolute;left:442px;top:180px;width:204px;text-align:center;font-size:34px;font-weight:400;color:var(--red)}
.site-footer{position:absolute;top:1147px;left:0;width:724px;height:53px;background:var(--dark);color:var(--white);font-family:'Arimo',sans-serif;font-size:8.4px;text-align:center;line-height:53px}
</style>
</head>
<body>

<section class="hero">
  <div class="hero-photo" role="img" aria-label="Photo of a business meeting with a pen pointing at a business report chart on a desk"></div>
  <h1 class="hero-title">QLV Advisors</h1>
  <p class="hero-sub">Modernize Your Harbor Ledger<sup>TM</sup><br>Get More Customers.</p>
  <form class="contact-card">
    <h2>GET IN TOUCH</h2>
    <div class="rule"></div>
    <div class="field" style="top:59px">First Name :</div>
    <div class="field" style="top:96px">Last Name :</div>
    <div class="field" style="top:133px">Email :</div>
    <div class="field message" style="top:170px">Message :</div>
    <div class="submit">SUBMIT</div>
  </form>
</section>

<header class="site-header">
  <div class="brand">QLV Advisors</div>
  <nav class="main-nav">
    <a class="active" style="left:304px">HOME</a>
    <a style="left:357px">SERVICES</a>
    <a style="left:426px">RESOURCES</a>
    <a style="left:504px">EVENTS</a>
    <a style="left:565px">BLOG</a>
    <a style="left:615px">ABOUT US</a>
  </nav>
</header>

<section class="services">
  <h2 class="section-title">OUR <em>SERVICES</em></h2>
  <div class="underline"></div>

  <article class="service-card" style="left:67px">
    <div class="service-icon">
      <svg width="82" height="82" viewBox="0 0 82 82" fill="none" stroke="#fff" stroke-width="1.8">
        <circle cx="41" cy="41" r="13"/><ellipse cx="41" cy="41" rx="6" ry="13"/><line x1="28" y1="41" x2="54" y2="41"/>
        <circle cx="23" cy="46" r="3"/><path d="M19 60v-7h8v7"/><circle cx="59" cy="24" r="3"/><path d="M55 38v-7h8v7"/>
      </svg>
    </div>
    <h3>OUTSOURCED SALES</h3>
    <p style="top:91px">We work with customers to map out profitable digital strategies to complement and enhance live events. Our expertise lies in iden tifying new revenue streams that allow customer experience</p>
  </article>

  <article class="service-card" style="left:216px">
    <div class="service-icon">
      <svg width="82" height="82" viewBox="0 0 82 82" fill="none" stroke="#fff" stroke-width="1.8">
        <rect x="25" y="18" width="20" height="13" rx="6"/><rect x="38" y="16" width="20" height="13" rx="6"/>
        <circle cx="30" cy="45" r="5"/><path d="M20 60c0-7 20-7 20 0z"/><circle cx="52" cy="45" r="5"/><path d="M42 60c0-7 20-7 20 0z"/>
      </svg>
    </div>
    <h3>HARBOR LEDGER<br>STRATEGIC CONSULTING</h3>
    <p style="top:107px">We work with customers to map out profitable digital strategies to complement and enhance live events. Our expertise lies in iden tifying new revenue streams</p>
  </article>

  <article class="service-card" style="left:365px">
    <div class="service-icon">
      <svg width="82" height="82" viewBox="0 0 82 82" fill="none" stroke="#fff" stroke-width="1.8">
        <rect x="25" y="20" width="32" height="28"/><line x1="22" y1="51" x2="60" y2="51"/><path d="M41 51l-8 8M41 51l8 8"/>
        <circle cx="32" cy="28" r="2"/><path d="M36 29l12-4"/><path d="M31 36l3 3M34 36l-3 3M45 38l4-4"/>
      </svg>
    </div>
    <h3>GRIDWEAVE STRATEGIC<br>CONSULTING</h3>
    <p style="top:107px">We work with customers to map out profitable digital strategies to complement and enhance live events. Our expertise lies in iden tifying new revenue streams</p>
  </article>

  <article class="service-card" style="left:514px">
    <div class="service-icon">
      <svg width="82" height="82" viewBox="0 0 82 82" fill="none" stroke="#fff" stroke-width="1.8">
        <circle cx="41" cy="36" r="14"/><circle cx="41" cy="36" r="10"/>
        <path d="M41 30l2 4 4 .5-3 3 .8 4-3.8-2-3.8 2 .8-4-3-3 4-.5z"/><path d="M31 46l-5 10 5-1 3 4 4-8M51 46l5 10-5-1-3 4-4-8"/>
      </svg>
    </div>
    <h3>QLV VIP</h3>
    <p style="top:91px">We work with customers to map out profitable digital strategies to complement and enhance live events. Our expertise lies in iden tifying new revenue streams that allow customer experience</p>
  </article>
</section>

<section class="welcome">
  <h2 class="section-title">WELCOME TO <em>QLV ADVISORS</em></h2>
  <div class="underline"></div>
  <p class="lead">QLV Advisors helps event and media companies as well as the technology partners that support them modernize revenue organizations and future proof their businesses. We created and trademarked The Harbor Ledger organizational model to help our customers achieve optimal and consistent sales acceleration and work with our clients to implement some or all of its core components depending on their unique business needs.</p>
  <p class="detail">We have deep expertise in the verticals we serve, and we understand the transformational shifts required to survive and thrive. Our services range from strategic consulting and interim sales leadership to satellite and full-funnel sales.We created and trademarked The Harbor Ledger organizational model to help our customers achieve optimal and consistent sales acceleration and work with our clients to implement some or all of its core components depending on their unique business needs.</p>
  <div class="welcome-brand">QLV Advisors</div>
</section>

<footer class="site-footer">© Copyrights 2021-QLV Advisors.All Rights Reserved.</footer>

</body>
</html>
```